Quill Ridge Business cards

We need business cards for our aviation company called Quill Ridge Aviation. The colour scheme is the same as the one in the logo you design (metallic green/ similar to the colours on the aircraft). The design needs to be unique and stand out.

Industry/Entity Type

Business

```html
<!DOCTYPE html>
<html lang="en">
<head>
<meta charset="utf-8">
<title>Quill Ridge Aviation — Business Cards</title>
<link rel="stylesheet" href="https://fonts.googleapis.com/css2?family=Archivo+Black&family=Poppins:wght@300&display=swap">
<style>
  :root {
    --stage: #e9ebea;
    --card: #f4f5f5;
    --card-edge: #e2e4e4;
    --ink: #111111;
    --text-muted: #3a3a3a;
    --green-dark: #1f6b2a;
    --green-mid: #3e9a3c;
    --green-light: #8cc751;
    --green-pale: #b5d97a;
  }
  * { box-sizing: border-box; margin: 0; padding: 0; }
  html, body {
    width: 1200px;
    height: 723px;
    overflow: hidden;
    background: var(--stage);
  }
  .sheet {
    width: 1200px;
    height: 723px;
    display: flex;
    align-items: center;
    justify-content: center;
    gap: 90px;
  }
  .card {
    position: relative;
    width: 350px;
    height: 600px;
    border-radius: 26px;
    background: linear-gradient(160deg, #fbfbfb 0%, var(--card) 55%, var(--card-edge) 100%);
    box-shadow: 0 10px 28px rgba(0,0,0,0.12);
    overflow: hidden;
  }
  .brand-name {
    font-family: "Archivo Black", sans-serif;
    color: var(--ink);
    letter-spacing: -0.3px;
    white-space: nowrap;
  }
  .brand-mark {
    display: inline-block;
    border-radius: 50%;
    background: var(--green-mid);
  }

  /* back side: contact details */
  .card-back .brand {
    position: absolute;
    top: 58px;
    right: 48px;
    display: flex;
    flex-direction: column;
    align-items: center;
    gap: 8px;
  }
  .card-back .brand-mark { width: 30px; height: 30px; }
  .card-back .brand-name { font-size: 13px; }
  .art-area {
    position: absolute;
    left: 0;
    top: 140px;
    width: 128px;
    height: 320px;
    background: linear-gradient(200deg, var(--green-pale) 0%, var(--green-light) 30%, var(--green-mid) 65%, var(--green-dark) 100%);
  }
  .contact-list {
    position: absolute;
    top: 205px;
    left: 150px;
    list-style: none;
    display: flex;
    flex-direction: column;
    gap: 30px;
  }
  .contact-item {
    display: flex;
    align-items: center;
    gap: 14px;
    font-family: "Poppins", sans-serif;
    font-weight: 300;
    font-size: 10.5px;
    color: var(--text-muted);
    white-space: nowrap;
  }
  .contact-icon { width: 20px; height: 20px; flex: none; }

  /* front side: brand */
  .card-front .brand {
    position: absolute;
    top: 120px;
    left: 0;
    right: 0;
    display: flex;
    flex-direction: column;
    align-items: center;
    gap: 18px;
  }
  .card-front .brand-mark { width: 54px; height: 54px; }
  .card-front .brand-name { font-size: 24px; }
</style>
</head>
<body>
<main class="sheet">

  <section class="card card-back" aria-label="Business card back">
    <div class="brand">
      <span class="brand-mark" aria-hidden="true"></span>
      <span class="brand-name">Quill Ridge Aviation</span>
    </div>

    <div class="art-area" role="img" aria-label="Large green faceted bird illustration"></div>

    <ul class="contact-list">
      <li class="contact-item">
        <svg class="contact-icon" viewBox="0 0 20 20" aria-hidden="true">
          <path d="M10 2a5.5 5.5 0 0 0-5.5 5.5C4.5 12 10 18 10 18s5.5-6 5.5-10.5A5.5 5.5 0 0 0 10 2z" fill="none" stroke="#222" stroke-width="1.4"/>
          <circle cx="10" cy="7.5" r="2" fill="none" stroke="#222" stroke-width="1.4"/>
        </svg>
        <span>your adress here</span>
      </li>
      <li class="contact-item">
        <svg class="contact-icon" viewBox="0 0 20 20" aria-hidden="true">
          <rect x="2" y="5" width="16" height="11" fill="none" stroke="#222" stroke-width="1.4"/>
          <path d="M2 5l8 6 8-6" fill="none" stroke="#222" stroke-width="1.4"/>
        </svg>
        <span>yourmail@yourmail.com</span>
      </li>
      <li class="contact-item">
        <svg class="contact-icon" viewBox="0 0 20 20" aria-hidden="true">
          <rect x="5.5" y="2" width="9" height="16" rx="1.5" fill="none" stroke="#222" stroke-width="1.4"/>
          <line x1="8.5" y1="15.5" x2="11.5" y2="15.5" stroke="#222" stroke-width="1.4"/>
        </svg>
        <span>12345678901234567</span>
      </li>
      <li class="contact-item">
        <svg class="contact-icon" viewBox="0 0 20 20" aria-hidden="true">
          <path d="M2 8c0-3 4-4 8-4s8 1 8 4l-3 1-1-2H6L5 9z" fill="#222"/>
          <rect x="4" y="10" width="12" height="7" rx="1" fill="#222"/>
          <circle cx="10" cy="13.5" r="2" fill="#fff"/>
        </svg>
        <span>12345678901234567</span>
      </li>
    </ul>
  </section>

  <section class="card card-front" aria-label="Business card front">
    <div class="brand">
      <span class="brand-mark" aria-hidden="true"></span>
      <span class="brand-name">Quill Ridge Aviation</span>
    </div>
  </section>

</main>
</body>
</html>
```